The Grove- All Natural Company Needs Packaging for Main Product

Aloha!

We are a natural products company from Kaua’i, Hawaii called “The Grove”

The first thing we need packaging for is for our all natural bug spray called “Natural Pest Ward”

We will need much more packaging for many other products in the future so we need a packaging design theme that will serve many products. Our other products are a Reef Safe Sunblock Face Stick called Face Shade
Reef Safe Sunblock Body Lotion called Body Shade and other future natural products.

Very Important:
We love all Tide Pup packaging for its simplicity and cleanness. We honestly want our packaging to be just like Tide Pup in its own way. Instead of having the monkey, we want our Grove logo to go in the middle like the monkey is on all Tide Pup packaging. We want everything else pretty much the same but just for Bug Spray. Though, we do not want to copy of course, but we would like it be similar.

Front Label- Needs to be on there: (Following guide of Tide Pup Front label)
1. Black Background
2. Grove logo
3. Make it look professional
4. Make it Clean
5. Make it pop on the shelf
6. Needs to say the following:

** Please not we changed the brief. We changed it so Natural Pest Ward all goes together on the front as one logo for
Natural
Bug
Grove

a. Natural Pest Ward (where Tide Pup is)
b. Grove Logo (where monkey is)
c. Deet-Free. (where Golden Blend is)
d. Bug Spray (in between 2 lines) (where Tress Brightener is)
e. Natural Bug Spray enriched (where it says Premium Hair enriched…)
with quality essential oils that
repels mosquitos, gnats, no seeums,
ticks and all other bitey things.
f. Made with Aloha (where it says Blonde to Medium Brown Hair Types)
g. 4 FL OZ/ 118 mL (under Blonde to Medium Brown Hair Types)

Back Label-Things need on there: (Following guide of Tide Pup Back Label)

1. We have given an example Tide Pup Back Label. We would like it to look very similar to it.
2. Make room for a small UPC code on back.
3. Needs to say:

The Grove products are naturally made for those to enjoy the outdoors.

Reef Safe Gluten Free Hypoallergenic Non-GMO
Deet Free Paraben Free Gluten Free Organic Ingredients

Product Description

Pest Ward is naturally enriched with quality essential oils to repel mosquitos, gnats, no seeums, ticks, and all other bites things. It is safe for babies, kids, and adults.

How to Use

Shake well and spray well on all parts of the body. Reapply every hour while outside.

Warning

Do not spray near or in eyes. If mistakenly sprayed in eyes, rinse with running water for 30 minutes.

Ingredients

Active Ingredients: Cedar wood oil (.35%) Citronella Oil (.30%) Eucalyptus Oil (.20%) Lemongrass Oil (.20%) Lavender Oil (.20%)
Inert Ingredients: Distilled Water, Coconut Oil, Witch Hazel

Exclusively Manufactured and Distributed by The Grove LLC, 2836 Wainohe Rd. Kilauea, Hawaii, 96754 USA © All Rights Reserved
Get more information at NaturalPestWard.example

Other Notes.
1. The label we’ve been using is 4”x5”
2. The Font we've been using for the Pest Ward logo part is Neutraface but we are glad to try other things that would make it look clean and stand out. Love the Tide Pup logo and font but definitely want something unique for us.

Attached:

Thank you for all your hard work on this project. Please let us know if you have any questions, and we look forward to seeing your amazing packaging design.

Thanks and Aloha!
The Grove Team

Target Market(s)

Retail Stores, Adventure Tours, Families

Industry/Entity Type

It Company

Font styles to use
Other font styles liked:
• Professional looking font

Colors
e34196
fbed22
00a990
000000
fbfbfb

Requirements
Must have
• Wrote everything above.
• Must Be VERY professional.
• Clean look.
• POP on a shelf.
• Creative
• White lettering to make it look clean with black background.
Nice to have
• Wrote everything above.
• Must be VERY professional.
• Clean look
• POP on a shelf
• Creative
Should not have
• Clutter
• not look professional
• distractions

```html
<!DOCTYPE html>
<html lang="en">
<head>
<meta charset="utf-8">
<title>Natural Pest Ward – Front Label</title>
<link rel="stylesheet" href="https://fonts.googleapis.com/css2?family=Montserrat:wght@400;500;600;700;800&family=Allura&display=swap">
<style>
  :root {
    --page: #fbfbfb;
    --label: #1b1b1b;
    --ink: #fbfbfb;
    --rule: #e6e6e6;
    --magenta: #e34196;
    --yellow: #fbed22;
    --teal: #00a990;
  }
  * { margin: 0; padding: 0; box-sizing: border-box; }
  html, body {
    width: 1200px; height: 1200px; overflow: hidden;
    background: var(--page);
  }
  .canvas { position: relative; width: 1200px; height: 1200px; }
  .label {
    position: absolute; left: 390px; top: 40px;
    width: 420px; height: 1120px;
    background: var(--label);
    color: var(--ink);
    font-family: "Montserrat", sans-serif;
  }
  .label > * { position: absolute; left: 90px; white-space: nowrap; }
  .tagline {
    top: 100px; left: 76px;
    font-family: "Allura", cursive;
    font-size: 30px; line-height: 1;
  }
  .brand-mark {
    top: 232px;
    display: flex; align-items: center; gap: 16px;
  }
  .brand-mark .square {
    width: 56px; height: 56px; background: var(--magenta); flex: none;
  }
  .brand-mark .name {
    font-weight: 700; font-size: 38px; line-height: 1; color: var(--ink);
  }
  .product-natural {
    top: 374px; font-weight: 600; font-size: 28px; line-height: 1; letter-spacing: 2px;
  }
  .product-name {
    top: 408px; font-weight: 800; font-size: 76px; line-height: 64px;
    letter-spacing: 2px;
  }
  .rule { width: 262px; height: 3px; background: var(--rule); }
  .rule.top { top: 541px; }
  .rule.mid { top: 625px; }
  .rule.bottom { top: 862px; }
  .repels {
    top: 558px; font-weight: 700; font-size: 44px; line-height: 52px;
  }
  .pest-list {
    top: 655px; list-style: none;
    font-weight: 600; font-size: 21px; line-height: 39px;
  }
  .deet-badge {
    top: 720px; left: 254px; width: 128px; height: 128px;
  }
  .made-with {
    top: 913px; font-weight: 700; font-size: 22px; line-height: 1; letter-spacing: 1px;
  }
  .volume {
    top: 1006px; font-weight: 400; font-size: 29px; line-height: 1;
  }
</style>
</head>
<body>
  <div class="canvas">
    <section class="label">
      <p class="tagline">All-Natural Organic</p>

      <div class="brand-mark">
        <span class="square"></span>
        <span class="name">The Grove</span>
      </div>

      <p class="product-natural">NATURAL</p>
      <h1 class="product-name">PEST<br>WARD</h1>
      <div class="rule top"></div>
      <p class="repels">REPELS</p>
      <div class="rule mid"></div>

      <ul class="pest-list">
        <li>MOSQUITOS</li>
        <li>NO SEEUMS</li>
        <li>GNAT</li>
        <li>TICKS</li>
        <li>BITEY THINGS</li>
      </ul>

      <svg class="deet-badge" viewBox="0 0 128 128" aria-label="DEET free">
        <circle cx="64" cy="64" r="62" fill="#fbfbfb"/>
        <circle cx="64" cy="64" r="54" fill="none" stroke="#1b1b1b" stroke-width="3"/>
        <text x="64" y="61" text-anchor="middle" font-family="Montserrat, sans-serif" font-weight="800" font-size="25" fill="#1b1b1b">DEET</text>
        <text x="64" y="88" text-anchor="middle" font-family="Montserrat, sans-serif" font-weight="800" font-size="25" fill="#1b1b1b">FREE</text>
      </svg>

      <div class="rule bottom"></div>
      <p class="made-with">MADE WITH ALOHA</p>
      <p class="volume">4oz.</p>
    </section>
  </div>
</body>
</html>
```